Business Card - high end, modern health care

Hey designers!

We need a double sided business card for the boutique, cutting edge physical therapy rehabilitation centre in Sydney's Northern Beaches.

With the most qualified physios in the area The Harbourline Motion Clinic does what other physiotherapy practices do not, we take our time with our patients giving them longer appointments, better physios and therefor faster results!

We guarantee that the service people receive at THMC will be unparalleled.

Hence we need a business card to reflect our modern, boutique, high end service. The final design needs to reflect that we are in a class of our own yet with the feel of beachside retreat.

Below I have attached our logo in both blue on white and white on blue. The exact colour is;
and the font that we have used in our logo is Tex Gyre Aventador.

I like the idea of the blue as the main colour as it is more eye catching and our signage onto the main road will be in this blue and in the interest of consistency across marketing the blue needs to be a part of the design. However I would appreciate a few designs onto a wooden background as this is a visual theme within the fitout of the practice.

The design needs to be of standard size (91x55mm).

Target Market(s)

We target people who have an end outcome in mind and those who have had poor experiences with other providers and ensure that everyone gets the care that they deserve with a premium service that is tailored to the individuals circumstances. As a premium service, the target market is highly educated, business and tech savvy with the additional target market of elderly people who have self funded their retirement and see value in paying for the best ongoing rehabilitation to maintain independence.

Industry/Entity Type

Physical Therapy

Contact Information for Business Card

Name, designation( Titled Musculoskeletal Physiotherapist... there will also be those in the company that have multiple designations ie 5 or 6 words long), phone number, email, facebook, instagram, address

Font styles to use
Sans Serif

Colors

Designer to choose colors to be used in the design.

Requirements
Must have
• Front - The logo as large as possible, blue or wooden theme, and all of the important details.
• Back - A blank space/lines on which to write appointment times (no "Appointment, date, time" etc.)
Nice to have
• facebook url
• logos for facebook and instagram
• Mini logos for the phone and email?

```html
<!DOCTYPE html>
<html lang="en">
<head>
<meta charset="utf-8">
<title>The Harbourline Motion Clinic – Business Card</title>
<link href="https://fonts.googleapis.com/css2?family=Roboto:wght@300;400;500&family=Roboto+Condensed:ital,wght@1,700&display=swap" rel="stylesheet">
<style>
  :root {
    --brand-blue: #0c56a3;
    --wave-blue: #2562ab;
    --wave-blue-soft: #1b5ca8;
    --ink-white: #ffffff;
  }
  html, body {
    margin: 0;
    padding: 0;
    width: 1200px;
    height: 686px;
    overflow: hidden;
    background: var(--brand-blue);
  }
  .card {
    position: relative;
    width: 1200px;
    height: 686px;
    background: var(--brand-blue);
    color: var(--ink-white);
    font-family: "Roboto", Arial, sans-serif;
    overflow: hidden;
  }
  .card__backdrop {
    position: absolute;
    inset: 0;
  }
  .brand {
    position: absolute;
    left: 83px;
    top: 78px;
    width: 1031px;
  }
  .brand__circle {
    position: absolute;
    left: 0;
    top: 0;
    width: 182px;
    height: 182px;
    border-radius: 50%;
    background: var(--ink-white);
  }
  .brand__name {
    position: absolute;
    left: 200px;
    right: 0;
    top: 6px;
    margin: 0;
    font-weight: 500;
    text-align: right;
    line-height: 1;
  }
  .brand__line-top {
    display: block;
    font-size: 71px;
    letter-spacing: 0.01em;
  }
  .brand__line-bottom {
    display: block;
    margin-top: 26px;
    font-size: 50px;
    letter-spacing: 0.24em;
    margin-right: -0.24em;
  }
  .address {
    position: absolute;
    right: 86px;
    top: 282px;
    margin: 0;
    font-size: 30px;
    font-weight: 300;
    font-style: normal;
  }
  .contact {
    position: absolute;
    left: 87px;
    top: 406px;
  }
  .contact__name {
    margin: 0;
    font-size: 30px;
    font-weight: 300;
  }
  .contact__role {
    margin: 16px 0 0;
    font-family: "Roboto Condensed", "Arial Narrow", sans-serif;
    font-style: italic;
    font-weight: 700;
    font-size: 30px;
  }
  .contact__line {
    display: flex;
    align-items: center;
    margin: 18px 0 0;
    font-size: 30px;
    font-weight: 300;
  }
  .contact__icon {
    flex: none;
    fill: var(--ink-white);
  }
  .contact__icon--phone { width: 36px; height: 38px; margin-right: 12px; }
  .contact__icon--mail { width: 52px; height: 32px; margin-right: 20px; }
</style>
</head>
<body>
  <main class="card">
    <svg class="card__backdrop" width="1200" height="686" viewBox="0 0 1200 686" aria-hidden="true">
      <circle cx="80" cy="-620" r="920" fill="none" stroke="var(--wave-blue-soft)" stroke-width="60" opacity="0.7"/>
      <circle cx="420" cy="1040" r="740" fill="var(--wave-blue)"/>
      <circle cx="560" cy="1180" r="600" fill="var(--brand-blue)"/>
    </svg>

    <header class="brand">
      <span class="brand__circle" aria-hidden="true"></span>
      <h1 class="brand__name">
        <span class="brand__line-top">THE HARBOURLINE</span>
        <span class="brand__line-bottom">MOTION CLINIC</span>
      </h1>
    </header>

    <address class="address">Address Line 1 Address Line 2 City, State, ZIP</address>

    <section class="contact">
      <p class="contact__name">First Name Last Name</p>
      <p class="contact__role">Titled Musculoskeletal Physiotherapist</p>
      <p class="contact__line">
        <svg class="contact__icon contact__icon--phone" viewBox="0 0 24 24" aria-hidden="true">
          <path d="M6.6 10.8a15.1 15.1 0 0 0 6.6 6.6l2.2-2.2a1 1 0 0 1 1-.25 11.4 11.4 0 0 0 3.6.57 1 1 0 0 1 1 1V20a1 1 0 0 1-1 1A17 17 0 0 1 3 4a1 1 0 0 1 1-1h3.5a1 1 0 0 1 1 1c0 1.25.2 2.45.57 3.57a1 1 0 0 1-.25 1z"/>
        </svg>
        <span>123 456 7890</span>
      </p>
      <p class="contact__line">
        <svg class="contact__icon contact__icon--mail" viewBox="0 0 52 32" aria-hidden="true">
          <path d="M0 0h52v32H0z M3 3v1.2l23 15 23-15V3z M3 7.8V29h46V7.8L26 22.8z" fill-rule="evenodd"/>
        </svg>
        <span>yourname@company.com</span>
      </p>
    </section>
  </main>
</body>
</html>
```